Design for a 3-4 screens mobile app

The app is a "simple" ordering mobile app.
1. START screen : user can select either "NEW order" either "VIEW history" - or, can access the usual Contact, About, and Conditions pages.
2. NEW order : is a sequence of 3 basic screens/forms made of 3-4 fields each. Logic is the following: you select the service you need, its recurrence, mention where you are located and then you post it towards the marketplace...
3. VIEW history : is where you land at the end of the ordering process - and accessible from START screen. You see there your previous orders, and their statuses.
Mandatory : we need design for START screen, NEW order and VIEW history screens.
Design but be optimized for Smartphones, used in Portrait mode.
Please take into account the design of the website promoting the Mobile App: https://tidyvanlane.be/
Optional but of course nice to have if you could propose some design or guidance for Contact, About, and Conditions pages...
Here attached a full screen sequence.
Updates
Thanks for all your proposals ! They were submitted to the final customer, he selects one ASAP !
Number of Pages Required
3 page
Look and feel
Each slider illustrates characteristics of the customer's brand and the style your logo design should communicate.

```html
<!DOCTYPE html>
<html lang="en">
<head>
<meta charset="utf-8">
<title>About – Tidy Van Lane</title>
<link rel="stylesheet" href="https://fonts.googleapis.com/css2?family=Fira+Sans:wght@300;500&display=swap">
<style>
  :root {
    --brand-orange: #fa6400;
    --divider-grey: #c9ccd0;
    --sky-top: #46a6ea;
    --sky-mid: #409fe6;
    --sky-bottom: #1f72bd;
    --text-white: #ffffff;
  }
  * { margin: 0; padding: 0; box-sizing: border-box; }
  html, body { width: 674px; height: 1200px; overflow: hidden; }
  body { font-family: "Fira Sans", sans-serif; background: var(--sky-top); }

  .app-screen {
    position: relative;
    width: 674px;
    height: 1200px;
    overflow: hidden;
    background: linear-gradient(180deg, var(--sky-top) 0%, var(--sky-mid) 60%, var(--sky-bottom) 100%);
  }

  .top-bar {
    position: absolute;
    left: 0; top: 0;
    width: 674px;
    height: 113px;
    background: var(--brand-orange);
    border-bottom: 4px solid var(--divider-grey);
  }
  .menu-button {
    position: absolute;
    left: 22px; top: 54px;
    width: 43px; height: 43px;
  }
  .screen-title {
    position: absolute;
    left: 0; right: 0; top: 52px;
    text-align: center;
    color: var(--text-white);
    font-weight: 500;
    font-size: 39px;
    line-height: 48px;
    letter-spacing: 1.5px;
  }

  .faq-item { position: absolute; left: 71px; width: 580px; color: var(--text-white); }
  .faq-question {
    font-weight: 500;
    font-size: 31px;
    line-height: 39px;
    letter-spacing: 0.6px;
    white-space: nowrap;
  }
  .faq-answer {
    font-weight: 300;
    font-size: 26.5px;
    line-height: 36.5px;
    letter-spacing: -0.3px;
    white-space: nowrap;
  }
  .faq-intro { top: 182px; }
  .faq-audience { top: 336px; }
  .faq-process { top: 598px; }
  .faq-payments { top: 862px; }
</style>
</head>
<body>
  <main class="app-screen">
    <header class="top-bar">
      <svg class="menu-button" viewBox="0 0 43 43" aria-label="Menu">
        <rect x="0" y="0" width="43" height="10" rx="5" fill="#ffffff"/>
        <rect x="0" y="16.5" width="43" height="10" rx="5" fill="#ffffff"/>
        <rect x="0" y="33" width="43" height="10" rx="5" fill="#ffffff"/>
      </svg>
      <h1 class="screen-title">ABOUT</h1>
    </header>

    <section class="faq-item faq-intro">
      <h2 class="faq-question">WHAT IS TIDY VAN LANE?</h2>
      <p class="faq-answer">The genius of home services. The first app to<br>link a service provider to&nbsp; a person.</p>
    </section>

    <section class="faq-item faq-audience">
      <h2 class="faq-question">WHAT IS IT FOR?</h2>
      <p class="faq-answer">For anyone who is looking for a housekeeper,<br>help with preparing your meals, an ironer, a<br>window cleaning aid, a shopping aid or<br>simply a replacement for your absent service<br>provider.</p>
    </section>

    <section class="faq-item faq-process">
      <h2 class="faq-question">HOW DOES IT WORK?</h2>
      <p class="faq-answer">It helps customers to find a home services<br>provider amongst more than 3333<br>companies. Helping you find the person<br>who will respond to your requests within<br>24 hours.</p>
    </section>

    <section class="faq-item faq-payments">
      <h2 class="faq-question">HOW DO PAYMENTS HAPPEN?</h2>
      <p class="faq-answer">quis nostrud exercitation ullamco laboris<br>nisi ut aliquip ex ea commodo consequat.<br>Duis aute irure dolor in reprehenderit in<br>voluptate velit esse cillum dolore eu fugiat<br>nulla pariatur.</p>
    </section>
  </main>
</body>
</html>
```